Stationery Design Project

Require letterhead/stationery design based on new logo (see attached).

Would prefer it kept simple but strong and effective.

Target Market(s)

Clients and building developers. Residential/consumer and corporate clientele.

```html
<!DOCTYPE html>
<html lang="en">
<head>
<meta charset="utf-8">
<title>Keystone Works Letterhead</title>
<link rel="stylesheet" href="https://fonts.googleapis.com/css2?family=Open+Sans:wght@700&display=swap">
<style>
  :root {
    --backdrop: #e8e6e3;
    --paper: #ffffff;
    --accent-blue: #3dbbea;
    --accent-grey: #8e9196;
    --ink: #1f2230;
    --rule: #111111;
  }
  * { margin: 0; padding: 0; box-sizing: border-box; }
  html, body {
    width: 1200px;
    height: 900px;
    overflow: hidden;
    background: var(--backdrop);
    font-family: "Open Sans", Arial, sans-serif;
  }
  .letterhead {
    position: absolute;
    left: 317px;
    top: 22px;
    width: 565px;
    height: 856px;
    background: var(--paper);
    box-shadow: 0 6px 24px rgba(0, 0, 0, 0.18);
    overflow: hidden;
  }
  .letterhead__trim {
    position: absolute;
    inset: 0;
    width: 100%;
    height: 100%;
  }
  .trim-blue { fill: var(--accent-blue); }
  .trim-grey { fill: var(--accent-grey); }

  .brand {
    position: absolute;
    right: 26px;
    top: 92px;
    display: flex;
    align-items: center;
    gap: 10px;
  }
  .brand__mark {
    width: 22px;
    height: 22px;
    background: var(--accent-blue);
  }
  .brand__name {
    font-size: 22px;
    font-weight: 700;
    letter-spacing: 1px;
    color: var(--accent-grey);
  }

  .contact-rule {
    position: absolute;
    left: 120px;
    top: 207px;
    width: 3px;
    height: 481px;
    background: var(--rule);
  }
  .contact-list {
    list-style: none;
  }
  .contact-item {
    position: absolute;
    left: 8px;
    width: 100px;
    display: flex;
    flex-direction: column;
    align-items: center;
    gap: 10px;
  }
  .contact-item--phone { top: 222px; }
  .contact-item--fax { top: 311px; }
  .contact-item--email { top: 411px; }
  .contact-item--website { top: 518px; }
  .contact-item__icon {
    width: 22px;
    height: 22px;
    fill: var(--accent-blue);
  }
  .contact-item__label {
    font-size: 15px;
    font-weight: 700;
    letter-spacing: -0.3px;
    color: var(--ink);
    line-height: 1;
  }
</style>
</head>
<body>
  <main class="letterhead">
    <svg class="letterhead__trim" viewBox="0 0 482 730" preserveAspectRatio="none" aria-hidden="true">
      <polygon class="trim-blue" points="0,0 482,0 482,16 66,16 0,74"/>
      <polygon class="trim-grey" points="0,0 60,0 0,52"/>
      <polygon class="trim-blue" points="0,730 482,730 482,642 398,714 0,714"/>
      <polygon class="trim-grey" points="482,667 482,730 410,730"/>
    </svg>

    <header class="brand">
      <span class="brand__mark"></span>
      <span class="brand__name">KEYSTONE WORKS</span>
    </header>

    <div class="contact-rule"></div>

    <ul class="contact-list">
      <li class="contact-item contact-item--phone">
        <svg class="contact-item__icon" viewBox="0 0 24 24" aria-hidden="true">
          <path d="M7 2h6c1.5 0 2.5 1 2.5 2.5v15c0 1.5-1 2.5-2.5 2.5H7v-6h4.5v-2H9V10h2.5V8H7z"/>
        </svg>
        <span class="contact-item__label">PHONE</span>
      </li>
      <li class="contact-item contact-item--fax">
        <svg class="contact-item__icon" viewBox="0 0 24 24" aria-hidden="true">
          <path d="M7 3h10v6H7z"/>
          <path d="M4 10h16v7H4zM7 14h10v1.5H7z"/>
          <path d="M6 18h12v3H6z"/>
        </svg>
        <span class="contact-item__label">FAX</span>
      </li>
      <li class="contact-item contact-item--email">
        <svg class="contact-item__icon" viewBox="0 0 24 24" aria-hidden="true">
          <path d="M2 5h20v14H2zM4 7v10h16V7l-8 6z" fill-rule="evenodd"/>
          <path d="M4 7h16l-8 6z"/>
        </svg>
        <span class="contact-item__label">EMAIL</span>
      </li>
      <li class="contact-item contact-item--website">
        <svg class="contact-item__icon" viewBox="0 0 24 24" aria-hidden="true">
          <circle cx="12" cy="12" r="10"/>
          <path d="M7 6c2 1 3 2 2 4s-3 1-4 3c2 1 3 3 2 5-2-1-4-4-4-6s1-4 4-6zM15 14c2 0 3 1 2 3s-3 2-4 1 0-4 2-4z" fill="#ffffff"/>
        </svg>
        <span class="contact-item__label">WEBSITE</span>
      </li>
    </ul>
  </main>
</body>
</html>
```